Website Design for Hudson Family Counsel – Clean, Warm, Professional

Maren Holbeck, Esq.
www.MarenTHolbeckLegal.example

I’m a New York City-based attorney and CPA with a reputation for providing thoughtful, high-integrity legal guidance in both estate planning and small business law. I’ve served over 500 clients, and maintain a perfect 5-star rating. Clients come to me for clarity, compassion, and results — and I want my new website to reflect that.

**🎯 WHAT I NEED:**
A clean, modern, and emotionally resonant website that highlights who I am, what I do, and why clients trust me. It must feel approachable and warm, but still professional and elegant — think Quorvex meets boutique Vantage Firm. Feminine but not frilly.

**🧩 CORE WEBSITE SECTIONS (Top Navigation):**

1. **Home** – Strong first impression, tagline, CTA (book a call)
Homepage Copy (Sample Layout)
Headline:
Trusted Legal Guidance for Families and Founders.

Subheading:
Whether you’re protecting what you’ve built or building what’s next, I help you navigate estate planning and business law with confidence, compassion, and clarity.

Tagline (beneath logo or footer):
Legal Clarity for Life and Business.
2. **About Maren** – Bio, personal approach, credentials
3. **Services**

* *Estate Planning*
* *Business Law*
4. **Who I Work With** – Ideal clients (parents, entrepreneurs, etc.)
5. **Testimonials** – Client praise and social proof
6. **Success Stories** – Highlighting wins and case types
7. **FAQs** – Warm and clear answers to common questions
8. **Blog** – Thought leadership and helpful tips
8.5 Events
9. **Contact / Book a Call** – Scheduling or contact form

**🖼 STYLE DIRECTION:**

* Clean white backgrounds, soft jewel tones or neutrals
* Professional headshots and personal branding assets available
* Emphasis on readability, trust, and ease of navigation - THIS NEEDS TO BE BUILT OUT SO IT IS TRUSTED BY AI!
* No harsh colors, no corporate/legal clichés (e.g., gavels or scales) - I MEAN THIS. I DO NOT WANT A BORING LAW WEBSITE WITH SCALES AND GAVELS
* Feminine edge (not pink-heavy), with strong hierarchy and callouts

**💡 DESIGN NOTES:**

* Mobile-first design required
* Should include space for video or welcome message
* Easy to update blog or CMS area preferred
* Built in a user-friendly platform like WordPress, Webflow, or similar
* Needs to feel elevated enough to support high-end flat fee packages

**📣 TONE:**
Smart. Warm. Sophisticated. Human.

**⚖️ FINAL DELIVERABLES:**

* Homepage + 5+ interior pages
* Desktop + mobile views
* Style guide (fonts, colors, buttons)
* Bonus if you can help with copy layout/structure (not just visuals)

**📍TARGET AUDIENCE:**

* Busy professionals and families in NYC
* Women and couples who want peace of mind
* Entrepreneurs and creatives needing solid legal support

Here is my current site: www.MarenTHolbeckLegal.example
And here is a second business I have: www.QuickDayCounselDesk.example

Target Market(s)

Families and business owners

Industry/Entity Type

Law

Number of Pages Required

5+ page

Font styles to use
Serif
Sans Serif
Script

Requirements
Must have
• This website must be built to be seen as trustworthy by AI.

```html
<!DOCTYPE html>
<html lang="en">
<head>
<meta charset="utf-8">
<title>Hudson Family Counsel — Maren Holbeck, Esq.</title>
<link href="https://fonts.googleapis.com/css2?family=Gelasio:wght@400;500;600&family=Lato:wght@400;700&family=Mrs+Saint+Delafield&display=swap" rel="stylesheet">
<style>
:root{
  --mauve:#7b6479;
  --lavender:#e5dde8;
  --lavender-soft:#ece6ef;
  --teal:#2f5e62;
  --teal-light:#4a8580;
  --text:#4a4a4a;
  --card-dark:#444;
  --gold:#e8b33b;
  --cream:#f3dea4;
  --line:#8c7b8b;
  --footer:#151515;
  --white:#fff;
}
*{box-sizing:border-box;margin:0;padding:0}
html,body{width:1200px;height:5333px;overflow:hidden}
body{font-family:"Lato",sans-serif;color:var(--text);background:var(--white);position:relative}
.script{font-family:"Mrs Saint Delafield",cursive}
section,header,footer{position:absolute;left:0;width:1200px;overflow:hidden}
.abs{position:absolute}
.btn{position:absolute;display:flex;align-items:center;justify-content:center;gap:8px;background:var(--teal);color:var(--white);font-size:11px;font-weight:700;border:2px solid var(--white);outline:1px solid var(--teal);height:30px}
.btn svg{width:14px;height:10px}
.photo{position:absolute}
.section-title{position:absolute;left:0;width:1200px;text-align:center;font-family:"Gelasio",serif;font-size:29px;color:#3a3a3a}

.site-nav{top:0;height:42px;background:var(--mauve)}
.brand{left:120px;top:11px;font-family:"Gelasio",serif;font-weight:400;color:var(--white);font-size:17px}
.nav-links{position:absolute;left:412px;top:15px;display:flex;gap:14px;font-size:11px;color:var(--white)}
.nav-links .active{text-decoration:underline}
.nav-cta{position:absolute;left:975px;top:9px;width:102px;height:25px;border:1px solid var(--white);background:var(--teal);color:#fff;font-size:10px;font-weight:700;display:flex;align-items:center;justify-content:center;gap:6px}

.hero{top:42px;height:630px;background:linear-gradient(180deg,#3a3c42 0%,#24262b 55%,#1c1d21 100%)}
.hero h1{position:absolute;left:120px;top:130px;font-family:"Gelasio",serif;font-weight:400;font-size:56px;line-height:70px;color:var(--white)}
.hero h1 .accent{color:var(--teal-light)}
.hero-sub{left:120px;top:346px;width:400px;font-size:11px;line-height:17px;color:#e8e8e8}
.hero-word{left:-8px;top:528px;font-family:"Gelasio",serif;font-weight:400;font-size:110px;line-height:110px;color:#eeeeee;white-space:nowrap}

.about{top:672px;height:559px;background:linear-gradient(135deg,#f8f8f7,#eeeded 60%,#f7f6f5)}
.about-frame{left:120px;top:58px;width:418px;height:418px;border:2px solid var(--line)}
.about-vert{left:1090px;top:20px;writing-mode:vertical-rl;font-family:"Gelasio",serif;font-size:92px;color:transparent;-webkit-text-stroke:1px #d6d3d3;white-space:nowrap}
.about-script{left:600px;top:115px;font-size:40px;color:#555}
.about h2{position:absolute;left:600px;top:160px;font-family:"Gelasio",serif;font-weight:400;font-size:29px;color:#3a3a3a}
.about p{position:absolute;left:600px;width:460px;font-size:10.5px;line-height:18px;color:#555}

.services{top:1231px;height:513px;background:var(--lavender)}
.services-frame{left:103px;top:159px;width:990px;height:290px;border:2px solid var(--line)}
.service-card{top:114px;width:470px;height:317px}
.service-label{position:absolute;left:24px;bottom:18px;color:#fff;font-size:17px;display:flex;align-items:baseline;gap:8px}
.service-label .num{font-family:"Gelasio",serif;font-size:24px;color:transparent;-webkit-text-stroke:1px #fff}

.partners{top:1744px;height:190px;background:#fff}
.partner-row{position:absolute;left:120px;top:76px;width:960px;display:flex;justify-content:space-between;align-items:center}
.partner{display:flex;align-items:center;gap:8px;font-family:"Gelasio",serif;font-size:13px;color:#2e3a55;font-weight:600}
.partner i{display:block;width:22px;height:22px;border-radius:50%;background:#c9cfd9}

.testimonials{top:1934px;height:574px;background:#fff}
.testi-frame{left:93px;top:52px;width:1010px;height:358px;border:2px solid var(--line)}
.testi-box{left:120px;top:11px;width:958px;height:345px;background:var(--lavender-soft)}
.testi-card{top:143px;width:278px;height:306px;background:var(--card-dark);padding:26px 22px 0}
.stars{color:var(--gold);font-size:12px;letter-spacing:1px}
.testi-card blockquote{font-family:"Gelasio",serif;font-size:16px;line-height:27.5px;color:#f1f1f1;margin-top:14px}
.testi-card cite{display:block;font-style:normal;font-size:10.5px;color:var(--gold);margin-top:14px}
.round-arrow{position:absolute;width:24px;height:24px;border:1px solid #999;border-radius:50%;display:flex;align-items:center;justify-content:center}

.success{top:2508px;height:498px;background:var(--mauve)}
.success h2{position:absolute;left:120px;top:40px;font-family:"Gelasio",serif;font-weight:400;font-size:29px;color:#fff}
.story-script{left:120px;top:96px;font-size:26px;color:#f1f1f1}
.success h3{position:absolute;left:120px;top:134px;font-family:"Gelasio",serif;font-weight:400;font-size:20px;color:var(--cream)}
.story-block{left:120px;width:420px;color:#fff;font-size:10.5px;line-height:17px}
.story-block b{display:block;font-size:12px;margin-bottom:3px}

.faq{top:3006px;height:511px;background:linear-gradient(135deg,#f7f7f6,#eeeeed 60%,#f8f7f6)}
.faq-open{left:203px;top:118px;width:792px;height:89px;background:#6d6d6d;color:#fff;padding:12px 40px}
.faq-open h4{font-weight:400;font-size:12px}
.faq-open p{font-size:9.5px;line-height:15px;margin-top:8px;color:#eee}
.faq-item{left:203px;width:792px;height:32px;border:1px solid var(--mauve);background:#fff;display:flex;align-items:center;justify-content:space-between;padding:0 40px;font-size:11px;color:#555}

.blogs{top:3517px;height:693px;background:#f1f1f1}
.blog-card{top:118px;width:470px;height:447px;background:#fff}
.blog-img{position:absolute;left:0;top:0;width:470px;height:250px}
.date-badge{position:absolute;left:18px;top:0;width:40px;height:54px;background:var(--teal);border:2px solid #fff;border-top:none;color:#fff;text-align:center;font-size:9px;padding-top:8px}
.date-badge span{display:block;font-family:"Gelasio",serif;font-size:20px;line-height:20px}
.blog-body{position:absolute;left:20px;top:282px;width:420px}
.blog-card h3{font-family:"Gelasio",serif;font-weight:400;font-size:17px;line-height:24px;color:#444;border-left:3px solid var(--teal);padding-left:14px}
.blog-card p{font-size:10px;line-height:18px;color:#555;margin-top:14px;padding-left:17px}
.read-more{position:absolute;left:37px;top:418px;font-size:10.5px;color:var(--teal);display:flex;gap:8px;align-items:center}

.contact{top:4210px;height:611px;background:#fff}
.contact-frame-l{left:120px;top:58px;width:532px;height:491px;border:2px solid var(--line)}
.contact-frame-r{left:672px;top:58px;width:406px;height:491px;border:2px solid var(--line)}
.contact h2{position:absolute;left:710px;top:92px;font-family:"Gelasio",serif;font-weight:400;font-size:29px;color:#3a3a3a}
.field{left:690px;width:335px;height:37px;border:1px solid #999;font-size:10.5px;color:#444;padding:10px 12px}
.submit{position:absolute;left:690px;top:472px;width:335px;height:35px;background:var(--teal);border:2px solid #fff;outline:1px solid var(--teal);color:#fff;font-size:11px;font-weight:700;display:flex;align-items:center;justify-content:center;gap:8px}

.cta-band{top:4821px;height:217px;background:radial-gradient(circle at 50% 50%,#336a6e,#254e52)}
.cta-band h2{position:absolute;left:0;width:1200px;top:48px;text-align:center;font-family:"Gelasio",serif;font-weight:400;font-size:30px;color:#fff}
.cta-band p{position:absolute;left:0;width:1200px;top:96px;text-align:center;font-size:11px;color:#eee}

.site-footer{top:5038px;height:295px;background:var(--footer);color:#ddd}
.footer-col{position:absolute;top:58px}
.footer-col h4{font-family:"Gelasio",serif;font-weight:400;font-size:15px;color:#fff;margin-bottom:22px}
.footer-col p,.footer-col li{font-size:9.5px;line-height:18px;color:#ccc;list-style:none}
.contact-line{display:flex;gap:12px;align-items:flex-start;margin-bottom:10px;font-size:9.5px;line-height:14px;color:#ccc}
.icon-dot{flex:none;width:20px;height:20px;border-radius:50%;background:#fff;display:flex;align-items:center;justify-content:center}
.footer-rule{left:0;top:244px;width:1200px;height:1px;background:#333}
.copyright{left:0;width:1200px;top:262px;text-align:center;font-size:9px;color:#bbb}
</style>
</head>
<body>

<header class="site-nav">
  <div class="abs brand">Hudson Family Counsel</div>
  <nav class="nav-links">
    <span class="active">Home</span><span>About</span><span>Services</span><span>Testimonials</span><span>Success Stories</span><span>Events</span><span>FAQ</span><span>Contact</span>
  </nav>
  <div class="nav-cta">Book a Call <svg width="12" height="9" viewBox="0 0 14 10"><path d="M0 5h12M8 1l4 4-4 4" stroke="#fff" fill="none" stroke-width="1.5"/></svg></div>
</header>

<section class="hero">
  <div class="photo" role="img" aria-label="Night skyline of New York City behind the hero" style="left:0;top:0;width:1200px;height:630px;background:linear-gradient(180deg,rgba(60,62,70,.6),rgba(25,26,30,.2)),linear-gradient(90deg,#2a2c31,#3a3c43 50%,#26272c)"></div>
  <h1><span class="accent">Trusted Legal</span><br>Guidance For Families<br>and Founders.</h1>
  <p class="abs hero-sub">Whether you're protecting what you've built or building what's next, I help you navigate estate planning &amp; business law with confidence, compassion, &amp; clarity.</p>
  <div class="btn" style="left:120px;top:406px;width:180px">Book a Free Consultation <svg viewBox="0 0 14 10"><path d="M0 5h12M8 1l4 4-4 4" stroke="#fff" fill="none" stroke-width="1.5"/></svg></div>
  <div class="abs hero-word">Hudson Family Counsel</div>
  <div class="photo" role="img" aria-label="Portrait of the attorney in a dark suit holding a laptop" style="left:700px;top:0;width:335px;height:630px;background:linear-gradient(180deg,#5c5552 0%,#2b2a2c 40%,#1b1b1e 100%)"></div>
</section>

<section class="about">
  <div class="abs about-vert">ABOUT US</div>
  <div class="abs about-frame"></div>
  <div class="photo" role="img" aria-label="The attorney smiling at her desk with a laptop" style="left:141px;top:79px;width:418px;height:397px;background:linear-gradient(135deg,#8a8174,#5a5650 55%,#3c3b3d)"></div>
  <div class="abs about-script script">About Us</div>
  <h2>Clarity. Compassion. Confidence.</h2>
  <p style="top:208px">Hi, I'm Maren Holbeck — attorney, CPA, and a fierce advocate for peace of mind. Over the past decade, I've helped more than 500 clients in New York City and beyond plan wisely, protect what matters, and make confident legal decisions for their families and businesses.</p>
  <p style="top:286px">My clients are busy professionals, parents, creatives, and entrepreneurs. They come to me not just for technical answers — but for guidance from someone they can trust and a process that feels human. I believe the law should serve your life, not complicate it. When I'm not working with clients, you can find me reading biographies, walking in Central Park, or spending time with my husband and our daughter. I believe legal planning should feel as personal as it is practical — and I'm honored every time a client trusts me with their most important goals.</p>
  <div class="btn" style="left:600px;top:416px;width:162px">Learn More About Us <svg viewBox="0 0 14 10"><path d="M0 5h12M8 1l4 4-4 4" stroke="#fff" fill="none" stroke-width="1.5"/></svg></div>
</section>

<section class="services">
  <div class="section-title" style="top:50px">Services</div>
  <div class="abs services-frame"></div>
  <div class="photo service-card" role="img" aria-label="Client signing estate planning documents" style="left:120px;background:linear-gradient(135deg,#3d4150,#1e2028 55%,#5a5d66)">
    <div class="service-label"><span class="num">01.</span>Estate Planning</div>
  </div>
  <div class="photo service-card" role="img" aria-label="Business team meeting in a glass office" style="left:608px;background:linear-gradient(135deg,#b9c2c8,#7e8a93 50%,#d4d7d8)">
    <div class="service-label"><span class="num">02.</span>Business Law</div>
  </div>
</section>

<section class="partners">
  <div class="partner-row">
    <div class="partner"><i></i>Harlow &amp; Finch</div>
    <div class="partner"><i></i>The Ashby Law Group</div>
    <div class="partner"><i></i>Marlowe &amp; Reyes</div>
    <div class="partner"><i></i>Penrose Whitcombe</div>
    <div class="partner"><i></i>Vantage Firm</div>
    <div class="partner"><i></i>Counsel Office</div>
  </div>
</section>

<section class="testimonials">
  <div class="abs testi-frame"></div>
  <div class="abs testi-box"></div>
  <div class="section-title" style="top:56px">Testimonial</div>
  <div class="round-arrow" style="left:131px;top:284px"><svg width="10" height="10" viewBox="0 0 10 10"><path d="M6 1L2 5l4 4" stroke="#888" fill="none"/></svg></div>
  <div class="round-arrow" style="left:1043px;top:284px"><svg width="10" height="10" viewBox="0 0 10 10"><path d="M4 1l4 4-4 4" stroke="#888" fill="none"/></svg></div>
  <div class="abs testi-card" style="left:166px">
    <div class="stars">★★★★★</div>
    <blockquote>As a founder, I've worked with plenty of professionals. Maren is in a league of her own. Her legal knowledge is top-notch, but it's her communication style and integrity that really stand out.</blockquote>
    <cite>— Jasmine R., Creative Director</cite>
  </div>
  <div class="abs testi-card" style="left:459px">
    <div class="stars">★★★★★</div>
    <blockquote>"As a small business owner, I needed someone who understood both legal and financial strategy. Maren brought clarity, professionalism, and a personal touch that made all the difference."</blockquote>
    <cite>– A.M., Mother of Two</cite>
  </div>
  <div class="abs testi-card" style="left:753px">
    <div class="stars">★★★★★</div>
    <blockquote>"I kept putting off estate planning because it felt intimidating. Working with Maren was like having a trusted friend walk me through everything, step-by-step. She's brilliant — and kind."</blockquote>
    <cite>- D.T., Tech Startup CEO</cite>
  </div>
  <div class="btn" style="left:532px;top:478px;width:136px">View All Review <svg viewBox="0 0 14 10"><path d="M0 5h12M8 1l4 4-4 4" stroke="#fff" fill="none" stroke-width="1.5"/></svg></div>
</section>

<section class="success">
  <div class="photo" role="img" aria-label="Two smiling professional women in light suits" style="left:590px;top:0;width:610px;height:498px;background:linear-gradient(135deg,#e8eef3,#b7c4d0 50%,#dfe5ea)"></div>
  <h2>Success Stories</h2>
  <div class="abs story-script script">Story :</div>
  <h3>A Young Family Finds Peace of Mind</h3>
  <div class="abs story-block" style="top:190px"><b>The Situation:</b>A couple with two small children had no will or guardianship plan in place — and were overwhelmed by conflicting advice online.</div>
  <div class="abs story-block" style="top:264px"><b>What We Did:</b>We created a full estate plan, including wills, a trust, guardianship documents, and healthcare directives — all in under three weeks online.</div>
  <div class="abs story-block" style="top:338px"><b>The Result:</b>They left our last meeting saying, "We finally feel like grown-ups. And we can breathe."</div>
  <div class="btn" style="left:124px;top:422px;width:110px">Learn More <svg viewBox="0 0 14 10"><path d="M0 5h12M8 1l4 4-4 4" stroke="#fff" fill="none" stroke-width="1.5"/></svg></div>
  <div class="round-arrow" style="left:64px;top:236px;border-color:#ddd"><svg width="10" height="10" viewBox="0 0 10 10"><path d="M6 1L2 5l4 4" stroke="#fff" fill="none"/></svg></div>
</section>

<section class="faq">
  <div class="section-title" style="top:56px">FAQ</div>
  <div class="abs faq-open">
    <h4>Do I really need an estate plan?</h4>
    <p>If you have children, own property, or care about what happens to your assets — yes. Estate planning isn't just for the ultra-wealthy. It's for anyone who wants to protect their loved ones, minimize stress, and make decisions on their own terms.</p>
  </div>
  <div class="abs faq-item" style="top:222px">What's the difference between a will and a trust?<svg width="10" height="6" viewBox="0 0 10 6"><path d="M1 1l4 4 4-4" stroke="#777" fill="none"/></svg></div>
  <div class="abs faq-item" style="top:270px">How long does it take to complete an estate plan?<svg width="10" height="6" viewBox="0 0 10 6"><path d="M1 1l4 4 4-4" stroke="#777" fill="none"/></svg></div>
  <div class="abs faq-item" style="top:319px">I just started a business. Do I need a lawyer right now?<svg width="10" height="6" viewBox="0 0 10 6"><path d="M1 1l4 4 4-4" stroke="#777" fill="none"/></svg></div>
  <div class="abs faq-item" style="top:368px">Can you help with guardianship planning for my kids?<svg width="10" height="6" viewBox="0 0 10 6"><path d="M1 1l4 4 4-4" stroke="#777" fill="none"/></svg></div>
  <div class="btn" style="left:540px;top:430px;width:120px">View All FAQ <svg viewBox="0 0 14 10"><path d="M0 5h12M8 1l4 4-4 4" stroke="#fff" fill="none" stroke-width="1.5"/></svg></div>
</section>

<section class="blogs">
  <div class="section-title" style="top:52px">Blogs</div>
  <article class="abs blog-card" style="left:120px">
    <div class="blog-img" role="img" aria-label="Two people shaking hands across a desk" style="background:linear-gradient(135deg,#d8d3cc,#8f877d 55%,#e4e1dc)"></div>
    <div class="date-badge"><span>29</span>March</div>
    <div class="blog-body">
      <h3>Estate Planning Isn't Just for the Wealthy</h3>
      <p>Many people think they don't "need" an estate plan unless they have millions in assets. In reality, everyone — especially parents — needs a few key documents in place. This post breaks down the must-haves in plain English: will, health care proxy, power of attorney, and more.</p>
    </div>
    <div class="read-more">Learn More <svg width="14" height="10" viewBox="0 0 14 10"><path d="M0 5h12M8 1l4 4-4 4" stroke="#2f5e62" fill="none"/></svg></div>
  </article>
  <article class="abs blog-card" style="left:608px">
    <div class="blog-img" role="img" aria-label="Person writing notes at a desk" style="background:linear-gradient(135deg,#e6e4e0,#9c9890 55%,#cfcac3)"></div>
    <div class="date-badge"><span>29</span>March</div>
    <div class="blog-body">
      <h3>What Happens If You Die Without a Will in New York ?</h3>
      <p>Dying without a will means the state decides who gets what — not you. This post explains NY's intestacy laws, what that might look like in real life, and how to avoid unnecessary stress for your loved ones.</p>
    </div>
    <div class="read-more">Learn More <svg width="14" height="10" viewBox="0 0 14 10"><path d="M0 5h12M8 1l4 4-4 4" stroke="#2f5e62" fill="none"/></svg></div>
  </article>
  <div class="btn" style="left:540px;top:608px;width:112px">View All Blog <svg viewBox="0 0 14 10"><path d="M0 5h12M8 1l4 4-4 4" stroke="#fff" fill="none" stroke-width="1.5"/></svg></div>
</section>

<section class="contact">
  <div class="abs contact-frame-l"></div>
  <div class="photo" role="img" aria-label="The attorney in a black suit holding a clipboard" style="left:170px;top:93px;width:436px;height:414px;background:linear-gradient(180deg,#f2f2f2,#d9d7d6 60%,#bdb9b8)"></div>
  <div class="abs contact-frame-r"></div>
  <h2>Contact Us</h2>
  <div class="abs field" style="top:164px">Name :</div>
  <div class="abs field" style="top:214px">Email :</div>
  <div class="abs field" style="top:264px">Address :</div>
  <div class="abs field" style="top:311px;height:140px">Message :</div>
  <div class="submit">Submit <svg width="14" height="10" viewBox="0 0 14 10"><path d="M0 5h12M8 1l4 4-4 4" stroke="#fff" fill="none" stroke-width="1.5"/></svg></div>
</section>

<section class="cta-band">
  <h2>You deserve clarity, compassion, &amp; results - let's talk.</h2>
  <p>Book a quick call to get clear on your options and how I can support you — no pressure, just perspective.</p>
  <div class="btn" style="left:548px;top:140px;width:104px">Book a Call <svg viewBox="0 0 14 10"><path d="M0 5h12M8 1l4 4-4 4" stroke="#fff" fill="none" stroke-width="1.5"/></svg></div>
</section>

<footer class="site-footer">
  <div class="footer-col" style="left:120px;width:190px">
    <h4>Hudson Family Counsel</h4>
    <p>After leading significant single-family offices, we founded Northgate Advisory in 2017 to address a critical gap in the market.</p>
  </div>
  <div class="footer-col" style="left:348px">
    <h4>Quick Links</h4>
    <ul><li>Home</li><li>About Us</li><li>Services</li><li>Testimonial</li><li>Faq</li><li>Contact Us</li></ul>
  </div>
  <div class="footer-col" style="left:503px;width:200px">
    <h4>Contact Us</h4>
    <div class="contact-line"><span class="icon-dot"><svg width="10" height="12" viewBox="0 0 10 12"><path d="M5 11s4-4 4-6.5A4 4 0 0 0 1 4.5C1 7 5 11 5 11z" fill="#151515"/></svg></span>Maren Holbeck, Esq., CPA<br>120 Linden Row, 4th Floor<br>New York, NY 10010</div>
    <div class="contact-line"><span class="icon-dot"><svg width="10" height="10" viewBox="0 0 10 10"><path d="M2 1l2 2-1 1.5a6 6 0 0 0 2.5 2.5L7 6l2 2-1.5 1.5C4 9 1 6 .5 2.5z" fill="#151515"/></svg></span>+1 (555) 014-2290</div>
    <div class="contact-line"><span class="icon-dot"><svg width="10" height="8" viewBox="0 0 10 8"><rect x=".5" y=".5" width="9" height="7" fill="none" stroke="#151515"/><path d="M.5 .5l4.5 4 4.5-4" fill="none" stroke="#151515"/></svg></span><span style="color:#6b8fc2">maren@marentholbecklegal.example</span></div>
  </div>
  <div class="footer-col" style="left:739px">
    <h4>Community</h4>
    <div class="contact-line" style="align-items:center"><span class="icon-dot"></span>Friendboard</div>
    <div class="contact-line" style="align-items:center"><span class="icon-dot"></span>Chirpline</div>
    <div class="contact-line" style="align-items:center"><span class="icon-dot"></span>Careerlink</div>
  </div>
  <div class="footer-col" style="left:881px;width:197px">
    <h4>Subscribe Newsletter</h4>
    <p>Subscribe to our newsletter</p>
    <div style="margin-top:10px;height:34px;border:1px solid #ccc;font-size:9px;color:#ccc;padding:11px 16px">Enter email...</div>
    <div style="margin-top:16px;height:34px;background:var(--teal);border:2px solid #fff;color:#fff;font-size:10.5px;font-weight:700;display:flex;align-items:center;justify-content:center;gap:8px">Subscribe <svg width="14" height="10" viewBox="0 0 14 10"><path d="M0 5h12M8 1l4 4-4 4" stroke="#fff" fill="none" stroke-width="1.5"/></svg></div>
  </div>
  <div class="abs footer-rule"></div>
  <div class="abs copyright">© 2025 Maren Holbeck, Esq., CPA. All rights reserved.</div>
</footer>

</body>
</html>
```